Photography Price List DL flyer

In need of a double sided DL flyer to list prices for a photography business that is in the real estate industry. Will need to include logo and be themed to match. Price details and contact information are in the pdf attached.

Below are links to the logo and photos that can be used on the flyer.

Logo
https://www.parcelnook.net/s/q7mwd2kfp0zltab/LogoFiles.zip?dl=0

Photos
https://www.parcelnook.net/s/h3vtr9gkw1jenoy/Website_Images.zip?dl=0
Updates

Sorry people the photo examples I put the wrong link. I have fixed it in the brief but the proper link is: https://www.parcelnook.net/s/h3vtr9gkw1jenoy/Website_Images.zip?dl=0

Also dimensions of a DL are 210mm x 99mm + 3m bleed. Thanks

Target Market(s)

Real estate agents

Industry/Entity Type

Business

Requirements
Must have
• Price lists and contact information

```html
<!DOCTYPE html>
<html lang="en">
<head>
<meta charset="utf-8">
<title>Brightframe Photos – DL Price Flyer</title>
<link rel="stylesheet" href="https://fonts.googleapis.com/css2?family=Lato:wght@400;700;900&family=Montserrat:wght@700;800&display=swap">
<style>
  :root {
    --navy: #1b2148;
    --pink: #e8696f;
    --green: #a6cf6a;
    --paper: #f1f1f1;
    --paper-edge: #dcdcdc;
    --stage: #efece8;
    --white: #ffffff;
  }
  * { margin: 0; padding: 0; box-sizing: border-box; }
  html, body { width: 1200px; height: 1071px; overflow: hidden; }
  body { background: var(--stage); position: relative; font-family: "Lato", sans-serif; }

  .flyer {
    position: absolute; top: 73px; width: 450px; height: 922px; overflow: hidden;
    background: radial-gradient(ellipse at 50% 45%, var(--white) 0%, var(--paper) 55%, var(--paper-edge) 100%);
    box-shadow: 0 6px 18px rgba(0,0,0,.25);
  }
  .flyer--front { left: 136px; }
  .flyer--back { left: 641px; }

  .band { position: absolute; left: 0; width: 100%; }
  .front-top { top: 0; height: 282px; background: var(--navy); }
  .front-rule { top: 808px; height: 16px; background: var(--navy); }
  .front-foot { top: 824px; height: 98px; background: linear-gradient(90deg, var(--pink), #ef8a8e); }
  .back-top { top: 0; height: 154px; background: var(--navy); }
  .back-top-rule { top: 154px; height: 8px; background: var(--pink); }
  .back-rule { top: 830px; height: 16px; background: var(--pink); }
  .back-foot { top: 846px; height: 76px; background: var(--navy); }

  .decor { position: absolute; inset: 0; width: 450px; height: 922px; }

  .brand {
    position: absolute; top: 88px; right: 150px;
    font-family: "Lato", sans-serif; font-weight: 900; font-size: 36px;
    letter-spacing: 1px; color: var(--pink);
  }

  .wheel-label {
    position: absolute; left: 224px; top: 411px; transform: translate(-50%, -50%);
    text-align: center; line-height: 1;
  }
  .wheel-label .real { display: block; font-family: "Montserrat", sans-serif; font-weight: 800; font-size: 38px; color: var(--green); }
  .wheel-label .estate { display: block; font-family: "Lato", sans-serif; font-weight: 700; font-size: 24px; color: var(--navy); letter-spacing: 1px; margin-top: 4px; }

  .business-name {
    position: absolute; top: 740px; left: 0; width: 100%; transform: translateY(-50%);
    text-align: center; font-family: "Montserrat", sans-serif; font-weight: 800; font-size: 38px;
    letter-spacing: -1px; color: var(--navy);
  }
  .business-name .accent { color: var(--pink); }

  .phone-pill {
    position: absolute; left: 68px; top: 745px; width: 307px; height: 63px;
    background: var(--navy); border-radius: 14px 14px 0 0;
    display: flex; align-items: center; justify-content: center; gap: 12px;
  }
  .phone-pill svg { width: 34px; height: 34px; }
  .phone-pill .number { font-family: "Montserrat", sans-serif; font-weight: 800; font-size: 34px; color: var(--pink); letter-spacing: -1px; }

  .contact-line {
    position: absolute; left: 0; width: 100%; transform: translateY(-50%);
    display: flex; align-items: center; justify-content: center; gap: 12px;
    font-family: "Lato", sans-serif; font-weight: 700; font-size: 21px; color: var(--white);
  }
  .front-foot-line { top: 870px; color: var(--navy); }
  .back-foot-line { top: 884px; }

  .price-line {
    position: absolute; left: 0; width: 100%; transform: translateY(-50%);
    text-align: center; font-family: "Lato", sans-serif; font-weight: 700; font-size: 31px;
    color: var(--pink); white-space: nowrap; line-height: 1;
  }
  .price-line .cost { color: var(--navy); }
  .price-line--head { color: var(--navy); font-weight: 900; font-size: 29px; letter-spacing: 1px; }
  .price-line--small { font-size: 25px; }
  .prices-title { font-family: "Montserrat", sans-serif; font-weight: 800; font-size: 54px; color: var(--navy); }
  .prices-sub { font-weight: 400; font-size: 23px; letter-spacing: 1px; }
</style>
</head>
<body>

<!-- Front side -->
<section class="flyer flyer--front">
  <div class="band front-top"></div>
  <div class="band front-rule"></div>
  <div class="band front-foot"></div>

  <svg class="decor" viewBox="0 0 450 922" aria-hidden="true">
    <circle cx="337" cy="106" r="34" fill="var(--pink)"/>
    <g fill="none" stroke="var(--green)" stroke-width="7">
      <path d="M71 212 V180 H103"/>
      <path d="M357 180 H389 V212"/>
    </g>
    <g fill="none" stroke="var(--navy)" stroke-width="7">
      <path d="M71 594 V622 H103"/>
      <path d="M357 622 H389 V594"/>
    </g>
  </svg>

  <div class="brand">BRIGHTFRAME</div>

  <svg class="decor" viewBox="0 0 450 922">
    <circle cx="224" cy="411" r="189" fill="var(--pink)"/>
    <defs>
      <linearGradient id="collageTone" x1="0" y1="0" x2="1" y2="1">
        <stop offset="0" stop-color="#8a6a55"/>
        <stop offset=".45" stop-color="#c9b9a6"/>
        <stop offset="1" stop-color="#5d7fa8"/>
      </linearGradient>
    </defs>
    <circle cx="224" cy="411" r="178" fill="var(--white)"/>
    <circle cx="224" cy="411" r="172" fill="url(#collageTone)" role="img" aria-label="Wheel of real estate photographs: house exteriors, interiors and a city skyline at dusk"/>
    <circle cx="224" cy="411" r="94" fill="var(--pink)"/>
    <circle cx="224" cy="411" r="88" fill="var(--navy)"/>
    <circle cx="224" cy="411" r="80" fill="var(--white)"/>
  </svg>

  <div class="wheel-label">
    <span class="real">REAL</span>
    <span class="estate">ESTATE</span>
  </div>

  <h1 class="business-name">BRIGHTFRAME <span class="accent">PHOTOS</span></h1>

  <div class="phone-pill">
    <svg viewBox="0 0 34 34" aria-hidden="true">
      <rect x="1" y="1" width="32" height="32" rx="6" fill="var(--white)"/>
      <path d="M11 8c1-1 2.5-1 3 .5l1.5 3.5c.4 1-.2 1.8-1 2.3l-1 .7c1 2.5 3 4.5 5.5 5.5l.7-1c.5-.8 1.3-1.4 2.3-1l3.5 1.5c1.5.5 1.5 2 .5 3l-1.5 1.5c-3 2-13-5-14.5-14.5z" fill="var(--navy)"/>
    </svg>
    <span class="number">0400 517 264</span>
  </div>

  <div class="contact-line front-foot-line">
    <svg width="24" height="16" viewBox="0 0 24 16" aria-hidden="true">
      <rect x="1" y="1" width="22" height="14" fill="var(--navy)"/>
      <path d="M1 1 L12 9 L23 1" fill="none" stroke="var(--pink)" stroke-width="2"/>
    </svg>
    <span>info@brightframephotos.com.au</span>
  </div>
</section>

<!-- Back side -->
<section class="flyer flyer--back">
  <div class="band back-top"></div>
  <div class="band back-top-rule"></div>
  <div class="band back-rule"></div>
  <div class="band back-foot"></div>

  <svg class="decor" viewBox="0 0 450 922">
    <g fill="none" stroke="var(--green)" stroke-width="7">
      <path d="M30 100 V68 H62"/>
      <path d="M178 68 H210 V100"/>
      <path d="M240 100 V68 H272"/>
      <path d="M388 68 H420 V100"/>
    </g>
    <g fill="none" stroke="var(--navy)" stroke-width="7">
      <path d="M30 238 V270 H62"/>
      <path d="M178 270 H210 V238"/>
      <path d="M240 238 V270 H272"/>
      <path d="M388 270 H420 V238"/>
    </g>
    <defs>
      <linearGradient id="bedroomTone" x1="0" y1="0" x2="0" y2="1">
        <stop offset="0" stop-color="#d8cbb8"/>
        <stop offset="1" stop-color="#f3efe8"/>
      </linearGradient>
      <linearGradient id="poolTone" x1="0" y1="0" x2="0" y2="1">
        <stop offset="0" stop-color="#5a7fae"/>
        <stop offset=".6" stop-color="#b7a58c"/>
        <stop offset="1" stop-color="#3aa6c9"/>
      </linearGradient>
    </defs>
    <circle cx="126" cy="169" r="83" fill="var(--pink)"/>
    <circle cx="126" cy="169" r="74" fill="var(--navy)"/>
    <circle cx="126" cy="169" r="70" fill="url(#bedroomTone)" role="img" aria-label="Photograph of a furnished bedroom"/>
    <circle cx="325" cy="169" r="83" fill="var(--pink)"/>
    <circle cx="325" cy="169" r="74" fill="var(--navy)"/>
    <circle cx="325" cy="169" r="70" fill="url(#poolTone)" role="img" aria-label="Photograph of a backyard pool and outdoor kitchen at dusk"/>
  </svg>

  <h2 class="price-line prices-title" style="top:330px">PRICES</h2>
  <p class="price-line prices-sub" style="top:371px">PHOTOGRAPHY</p>
  <p class="price-line" style="top:417px">10 IMAGES <span class="cost">$149</span></p>
  <p class="price-line" style="top:453px">12 -15IMAGES <span class="cost">$179</span></p>
  <p class="price-line" style="top:490px">20+IMAGES <span class="cost">$229</span></p>
  <p class="price-line price-line--head" style="top:541px">TWILIGHT</p>
  <p class="price-line price-line--small" style="top:580px">ADD <span class="cost">$100</span> TO IMAGE PACKAGE</p>
  <p class="price-line price-line--head" style="top:626px">FLOORPLANS-$49</p>
  <p class="price-line price-line--head" style="top:671px">VIDEO</p>
  <p class="price-line" style="top:717px">30 SECONDS <span class="cost">$150</span></p>
  <p class="price-line" style="top:753px">60 SECONDS <span class="cost">$200</span></p>
  <p class="price-line" style="top:790px">2 MINUTES <span class="cost">$300</span></p>

  <div class="contact-line back-foot-line">
    <svg width="20" height="20" viewBox="0 0 20 20" aria-hidden="true">
      <g fill="none" stroke="var(--pink)" stroke-width="1.6">
        <circle cx="10" cy="10" r="8.5"/>
        <ellipse cx="10" cy="10" rx="3.8" ry="8.5"/>
        <path d="M1.5 10 H18.5 M3 5.5 H17 M3 14.5 H17"/>
      </g>
    </svg>
    <span>brightframephotos.com.au</span>
  </div>
</section>

</body>
</html>
```